Website for an interior designer

We need a new website for Clara Beth Holloway whose new business name is Clara Beth Holloway Interiors. She is a residential interior designer with a mix of modern and contemporary tastes. We are in the process of overhauling her website which is +15 years old and not an accurate reflection of her tastes. The uploaded photos are from some of the houses she has done as well as her logo(s). We would need a section for "About Us" that would have a paragraph of text and bullets showing services and a gallery for photos (~12 total, more to come). A contract page would be optional. The client likes the feel/look of this website: https://www.pondrickstudio.example/ but doesn't want to copy it exactly.

Target Market(s)

Upscale home owners

Industry/Entity Type

Interior Design

Coding

Coded - Design and coding required

Number of Pages Required

4 page

Colors

Designer to choose only greyscale colors for use in the design.

Requirements
Must have
• Home page, about us page, gallery page, contact us page.

```html
<!DOCTYPE html>
<html lang="en">
<head>
<meta charset="utf-8">
<title>Clara Beth Holloway Interiors</title>
<link rel="stylesheet" href="https://fonts.googleapis.com/css2?family=Cinzel:wght@400;500&family=Lato:wght@400;700&display=swap">
<style>
:root{
  --ink:#2e2e2e;
  --text:#555;
  --muted:#777;
  --hero-bg:#efefef;
  --white:#fff;
  --dark:#333;
  --panel:#e3e3e3;
  --field:#f2f2f2;
  --footer:#4a4a4a;
  --rule:#d8d8d8;
  --heading:"Cinzel", serif;
  --body:"Lato", sans-serif;
}
*{margin:0;padding:0;box-sizing:border-box}
html,body{width:1200px;height:3750px;overflow:hidden}
body{position:relative;background:var(--white);font-family:var(--body);color:var(--text)}
.abs{position:absolute}
.section{position:absolute;left:0;width:1200px}

/* header */
.site-header{top:0;height:99px;background:var(--hero-bg);border-bottom:1px solid var(--rule)}
.brand{left:234px;top:26px;width:214px;text-align:center;font-family:var(--heading);color:var(--ink)}
.brand-name{font-size:17px;letter-spacing:1px;display:block}
.brand-sub{font-size:9px;letter-spacing:5px;display:block;margin-top:6px}
.main-nav{top:40px;left:640px;display:flex;gap:0;font-family:var(--heading);font-size:11px;color:var(--ink);letter-spacing:.5px}
.main-nav a{position:absolute;white-space:nowrap;color:inherit;text-decoration:none}
.main-nav .active{border-bottom:1px solid var(--ink);padding-bottom:2px;font-size:12px}

/* hero */
.hero{top:99px;height:575px;background:var(--hero-bg)}
.hero-kicker{left:233px;top:178px;font-family:var(--heading);font-size:14px;color:var(--ink);letter-spacing:.5px}
.hero-title{left:232px;top:198px;font-family:var(--heading);font-size:42px;font-weight:500;color:var(--ink);letter-spacing:1px}
.btn-solid{left:234px;top:262px;width:159px;height:47px;background:var(--dark);color:var(--white);font-size:11px;letter-spacing:.5px;display:flex;align-items:center;justify-content:center}
.hero-photo{left:594px;top:68px;width:606px;height:438px;background:linear-gradient(160deg,#e9e7e1,#cfcbc2 55%,#7d6b57)}
.hero-dots{left:575px;top:541px;display:flex;gap:8px}
.hero-dots span{width:12px;height:2px;background:#bbb}
.hero-dots span.on{background:var(--ink)}

/* welcome */
.welcome{top:674px;height:507px;background:var(--white)}
.welcome-frame{left:258px;top:108px;width:259px;height:322px;border:3px solid var(--ink)}
.welcome-photo{left:287px;top:76px;width:284px;height:323px;background:linear-gradient(135deg,#f4f4f2,#d9d7d2 60%,#6b5e51)}
.welcome-title{left:626px;top:100px;font-family:var(--heading);font-size:32px;color:var(--ink);letter-spacing:1px}
.rule{height:2px;width:26px;background:var(--ink)}
.welcome-copy{left:628px;top:192px;width:345px;font-size:10px;line-height:19px;color:var(--muted)}
.welcome-copy p+p{margin-top:18px}
.btn-line{width:159px;height:49px;border:1px solid var(--ink);color:var(--ink);font-size:11px;display:flex;align-items:center;justify-content:center;letter-spacing:.5px}

/* specialization */
.special{top:1181px;height:675px;background:var(--dark);color:var(--white)}
.special-title{left:0;width:1200px;top:70px;text-align:center;font-family:var(--heading);font-size:34px;letter-spacing:2px}
.special-rule{left:587px;top:139px;width:26px;height:2px;background:var(--white)}
.special-lead{left:0;width:1200px;top:176px;text-align:center;font-size:13.5px;line-height:25px}
.special-head{left:234px;top:310px;font-family:var(--heading);font-size:19px;line-height:25px;letter-spacing:.5px}
.special-copy{left:234px;top:384px;width:340px;font-size:9.5px;line-height:19px}
.special .btn-line{border-color:var(--white);color:var(--white);left:234px;top:483px;height:50px}
.arrow{top:415px}
.special-frame{left:678px;top:279px;width:260px;height:325px;border:2px solid #8a8a8a}
.special-shade{left:910px;top:330px;width:52px;height:229px;background:#2b2b2b}
.special-photo{left:626px;top:250px;width:284px;height:323px;background:linear-gradient(170deg,#f3ecc8,#d88aa0 55%,#5b3a3a)}

/* gallery */
.gallery{top:1856px;height:1085px;background:var(--white)}
.gallery-title{left:0;width:1200px;top:70px;text-align:center;font-family:var(--heading);font-size:31px;color:var(--ink);letter-spacing:1.5px}
.gallery-rule{left:587px;top:132px}
.tile{position:absolute}
.tile-1{left:93px;top:168px;width:332px;height:499px;background:linear-gradient(160deg,#8c8f93,#54575b 60%,#3b3b3d)}
.tile-2{left:434px;top:168px;width:332px;height:499px;background:linear-gradient(160deg,#6f6f6f,#5a5a5a)}
.tile-3{left:775px;top:168px;width:332px;height:499px;background:linear-gradient(160deg,#ecebe7,#c7c5c0 60%,#3a3430)}
.tile-4{left:95px;top:676px;width:499px;height:333px;background:linear-gradient(135deg,#e6e6e4,#c9cac9 60%,#6a5a4a)}
.tile-5{left:604px;top:676px;width:501px;height:333px;background:linear-gradient(180deg,#eeeeee,#b7b2ab 60%,#5e7047)}
.tile-zoom{left:144px;top:228px}

/* contact */
.contact{top:2941px;height:676px;background:var(--panel)}
.contact-frame{left:116px;top:102px;width:402px;height:495px;border:3px solid var(--ink)}
.contact-photo{left:156px;top:73px;width:415px;height:481px;background:linear-gradient(160deg,#6d7a5a,#4f5647 50%,#3a3530)}
.contact-title{left:630px;width:475px;top:70px;text-align:center;font-family:var(--heading);font-size:30px;color:var(--ink);letter-spacing:1px}
.contact-rule{left:855px;top:133px}
.contact-lead{left:630px;width:475px;top:168px;text-align:center;font-size:13px;line-height:20px;color:var(--text)}
.contact-lead strong{color:var(--ink);font-weight:700}
.field{position:absolute;background:var(--field);border:1px solid #dcdcdc;font-size:10px;color:var(--ink);padding:13px 14px}
.btn-submit{left:628px;top:550px;width:478px;height:50px;background:var(--dark);color:var(--white);font-size:11px;display:flex;align-items:center;justify-content:center;letter-spacing:.5px}

/* footer */
.site-footer{top:3617px;height:105px;background:var(--footer);color:var(--white)}
.footer-nav a{position:absolute;top:32px;font-family:var(--heading);font-size:11px;color:var(--white);text-decoration:none;letter-spacing:.5px;white-space:nowrap}
.social{left:477px;top:62px;display:flex;gap:8px}
.social span{width:22px;height:22px;border-radius:50%;background:#9a9a9a}
.copyright{top:3722px;height:28px;background:var(--dark);color:#ddd;font-size:9.5px;display:flex;align-items:center;justify-content:center}
</style>
</head>
<body>

<header class="section site-header">
  <div class="abs brand">
    <span class="brand-name">CLARA BETH HOLLOWAY</span>
    <span class="brand-sub">INTERIORS</span>
  </div>
  <nav class="abs main-nav" style="left:0;top:0">
    <a class="active" href="#" style="left:640px;top:39px">Home</a>
    <a href="#" style="left:711px;top:41px">ABOUT US</a>
    <a href="#" style="left:805px;top:41px">GALLERY</a>
    <a href="#" style="left:887px;top:41px">CONTACT US</a>
  </nav>
</header>

<section class="section hero">
  <p class="abs hero-kicker">INTERIOR DESIGN FOR</p>
  <h1 class="abs hero-title">LIVING ROOM.</h1>
  <a class="abs btn-solid">CONTACT NOW!</a>
  <div class="abs hero-photo" role="img" aria-label="Bright living room with white sofas, beamed ceiling and tall steel-framed windows"></div>
  <div class="abs hero-dots"><span></span><span class="on"></span><span></span></div>
</section>

<section class="section welcome">
  <div class="abs welcome-frame"></div>
  <div class="abs welcome-photo" role="img" aria-label="White entry hall with a curving staircase and a small round table"></div>
  <h2 class="abs welcome-title">Welcome To CBH</h2>
  <div class="abs rule" style="left:628px;top:160px"></div>
  <div class="abs welcome-copy">
    <p>Clara Beth Holloway has extensive experience in all aspects of interior design. She has worked on a wide array of residential and commercial projects in her hometown of Houston and across the United States.</p>
    <p>Clara Beth's taste can best be described as a sophisticated blend of modern and traditional styles that combine to create a clean, timeless space.</p>
  </div>
  <a class="abs btn-line" style="left:628px;top:328px">READ MORE »</a>
</section>

<section class="section special">
  <h2 class="abs special-title">OUR SPECIALLIZATION</h2>
  <div class="abs special-rule"></div>
  <p class="abs special-lead">She has worked on a wide array of residential and commercial projects in her<br>hometown of Houston and across the United States.</p>
  <h3 class="abs special-head">Concept Origination and<br>Project Management</h3>
  <p class="abs special-copy">Duis autem vel eum iriure dolor in hendrerit in vulputate velit esse molestie consequat, vel illum dolore eu feugiat nulla facilisis at vero eros et accumsan et iusto odio dignissim qui blandit praesent luptatum zzril delenit augue duis dolore te feugait nulla facilisi.</p>
  <a class="abs btn-line">READ MORE »</a>
  <svg class="abs arrow" style="left:170px" width="32" height="18" viewBox="0 0 32 18" aria-hidden="true"><path d="M31 9H2M9 2L2 9l7 7" fill="none" stroke="#aaa" stroke-width="2"/></svg>
  <svg class="abs arrow" style="left:997px" width="32" height="18" viewBox="0 0 32 18" aria-hidden="true"><path d="M1 9h29M23 2l7 7-7 7" fill="none" stroke="#fff" stroke-width="2"/></svg>
  <div class="abs special-shade"></div>
  <div class="abs special-frame"></div>
  <div class="abs special-photo" role="img" aria-label="Staircase with colourful painted steps beside a yellow abstract artwork"></div>
</section>

<section class="section gallery">
  <h2 class="abs gallery-title">OUR CREATIVE PROJECT GALLERY</h2>
  <div class="abs rule gallery-rule"></div>
  <div class="tile tile-1" role="img" aria-label="Grey study with built-in bookshelves, fireplace and glass coffee table"></div>
  <div class="tile tile-2" role="img" aria-label="Soft white sitting area with a round table and framed art">
    <svg class="abs tile-zoom" width="44" height="44" viewBox="0 0 44 44" aria-hidden="true"><circle cx="22" cy="22" r="20" fill="none" stroke="#fff" stroke-width="2.5"/><path d="M22 12v20M12 22h20" stroke="#fff" stroke-width="3"/></svg>
  </div>
  <div class="tile tile-3" role="img" aria-label="White dining area with a brass pendant light and modern kitchen"></div>
  <div class="tile tile-4" role="img" aria-label="White marble kitchen with steel range hood and island"></div>
  <div class="tile tile-5" role="img" aria-label="White brick covered patio with lanterns and outdoor seating"></div>
</section>

<section class="section contact">
  <div class="abs contact-frame"></div>
  <div class="abs contact-photo" role="img" aria-label="Studio glass door with the business name, trees reflected behind"></div>
  <h2 class="abs contact-title">Let's Work Together</h2>
  <div class="abs rule contact-rule"></div>
  <p class="abs contact-lead">Use the form below to drop us an <strong>info@clarabethholloway.example</strong>.<br>Old-fashioned phone calls work too~ <strong>0100 555 0199</strong> and Launch your<br>Construction Project</p>
  <div class="field" style="left:630px;top:252px;width:230px;height:38px">Name *</div>
  <div class="field" style="left:875px;top:252px;width:230px;height:38px">Email *</div>
  <div class="field" style="left:630px;top:304px;width:230px;height:38px">Phone *</div>
  <div class="field" style="left:875px;top:304px;width:230px;height:38px">Services *</div>
  <div class="field" style="left:630px;top:357px;width:475px;height:178px">Messages *</div>
  <a class="abs btn-submit">SUBMIT</a>
</section>

<footer class="section site-footer">
  <nav class="footer-nav">
    <a href="#" style="left:432px">Home</a>
    <a href="#" style="left:502px">ABOUT US</a>
    <a href="#" style="left:595px">GALLERY</a>
    <a href="#" style="left:677px">CONTACT US</a>
  </nav>
  <div class="abs social" aria-label="Social links">
    <span></span><span></span><span></span><span></span><span></span><span></span><span></span><span></span>
  </div>
</footer>
<div class="section copyright">© 2002-2020 Clara Beth Holloway. All rights reserved.</div>

</body>
</html>
```